Just upload my Logo
Simple
Elsa Marroquín
quillmarshimages@postnook.net
Follow me in Chatterloom
* Wedding
* Engagment
* Maternity
* Newborn
* Family
* Events......etc

```html
<!DOCTYPE html>
<html lang="en">
<head>
<meta charset="utf-8">
<title>Elsa Marroquín – Business Card</title>
<link rel="stylesheet" href="https://fonts.googleapis.com/css2?family=Open+Sans:wght@400;600&display=swap">
<style>
  :root {
    --bg: #f1e6ea;
    --card: #ffffff;
    --charcoal: #3b3b3d;
    --magenta: #e4137f;
    --pink-text: #e0418f;
    --link-blue: #2f62b3;
    --ink: #1c1c1c;
    --faint: rgba(150,150,150,0.26);
    --faint-dark: rgba(255,255,255,0.14);
  }
  * { box-sizing: border-box; margin: 0; padding: 0; }
  html, body { width: 1200px; height: 940px; overflow: hidden; }
  body {
    background: var(--bg);
    font-family: "Open Sans", Arial, sans-serif;
    position: relative;
  }
  .card {
    position: absolute;
    left: 320px;
    width: 560px;
    height: 312px;
    background: var(--card);
    border: 2px solid var(--ink);
    border-radius: 18px;
    overflow: hidden;
  }
  .card--front { top: 140px; }
  .card--back { top: 488px; }

  .front-shape { position: absolute; inset: 0; }

  .logo-art {
    position: absolute;
    left: 28px; top: 92px;
    width: 120px; height: 74px;
    border-radius: 6px;
    background: linear-gradient(135deg, #d9d4d6, #b7aeb2 60%, #e9a9c8);
  }
  .logo-name {
    position: absolute;
    left: 28px; top: 172px;
    font-size: 20px;
    font-weight: 600;
    color: var(--pink-text);
    line-height: 1.1;
    white-space: nowrap;
  }

  .holder-name {
    position: absolute;
    right: 26px; top: 22px;
    font-size: 27px;
    font-weight: 400;
    color: #ffffff;
  }
  .faint-mark {
    position: absolute;
    font-weight: 600;
    white-space: nowrap;
  }
  .faint-mark--front {
    left: 318px; top: 122px;
    font-size: 22px;
    color: var(--faint-dark);
  }
  .contact {
    position: absolute;
    left: 296px;
    display: flex; align-items: center; gap: 9px;
    font-size: 12px;
    color: #ffffff;
  }
  .contact--phone { top: 236px; }
  .contact--email { top: 266px; }
  .contact svg { flex: none; }

  .follow {
    position: absolute;
    left: 96px; top: 26px;
    display: flex; align-items: center; gap: 10px;
    font-size: 16px;
    color: var(--link-blue);
  }
  .follow-square {
    width: 24px; height: 24px;
    border-radius: 4px;
    background: var(--link-blue);
  }
  .faint-art {
    position: absolute;
    left: 18px; top: 96px;
    width: 86px; height: 84px;
    border-radius: 6px;
    background: linear-gradient(135deg, #ececec, #dcdcdc);
  }
  .faint-mark--back {
    left: 130px; top: 200px;
    font-size: 32px;
    color: var(--faint);
  }
  .services {
    position: absolute;
    left: 118px; top: 64px;
    list-style: none;
    font-size: 15px;
    line-height: 22px;
    color: var(--pink-text);
  }
  .services li::before { content: "* "; }
  .back-email {
    position: absolute;
    left: 0; right: 0; bottom: 14px;
    display: flex; justify-content: center; align-items: center; gap: 8px;
    font-size: 12px;
    color: var(--ink);
  }
</style>
</head>
<body>

<section class="card card--front" aria-label="Business card front">
  <svg class="front-shape" width="560" height="312" viewBox="0 0 560 312" aria-hidden="true">
    <path d="M262 0 H560 V312 H214 C252 240 272 110 262 0 Z" fill="var(--charcoal)"/>
    <path d="M252 0 C262 110 244 236 204 312" fill="none" stroke="var(--magenta)" stroke-width="14"/>
  </svg>

  <div class="logo-art" role="img" aria-label="Illustrated bird perched on a swirling floral ornament"></div>
  <div class="logo-name">Quillmarsh Images</div>

  <h1 class="holder-name">Elsa Marroquín</h1>
  <div class="faint-mark faint-mark--front" aria-hidden="true">Quillmarsh Images</div>

  <div class="contact contact--phone">
    <svg width="16" height="16" viewBox="0 0 16 16" aria-hidden="true">
      <rect x="1" y="2" width="14" height="12" rx="2" fill="#fff"/>
      <path d="M4 5 h3 v6 h-3z M9 5 h3 M9 8 h3 M9 11 h3" stroke="var(--charcoal)" stroke-width="1.3" fill="none"/>
    </svg>
    <span>(555) 014-2273</span>
  </div>
  <div class="contact contact--email">
    <svg width="16" height="16" viewBox="0 0 16 16" aria-hidden="true">
      <circle cx="8" cy="8" r="7" fill="#fff"/>
      <rect x="4" y="5.5" width="8" height="5.5" fill="none" stroke="var(--charcoal)" stroke-width="1.2"/>
      <path d="M4 5.5 L8 8.5 L12 5.5" fill="none" stroke="var(--charcoal)" stroke-width="1.2"/>
    </svg>
    <span>quillmarshimages@postnook.net</span>
  </div>
</section>

<section class="card card--back" aria-label="Business card back">
  <div class="follow"><span class="follow-square" aria-hidden="true"></span><span>Follow me in Chatterloom</span></div>

  <div class="faint-art" role="img" aria-label="Faint bird and floral ornament decoration"></div>
  <div class="faint-mark faint-mark--back" aria-hidden="true">Quillmarsh Images</div>

  <ul class="services">
    <li>Wedding</li>
    <li>Engagment</li>
    <li>Maternity</li>
    <li>Newborn</li>
    <li>Family</li>
    <li>Events......etc</li>
  </ul>

  <div class="back-email">
    <svg width="16" height="16" viewBox="0 0 16 16" aria-hidden="true">
      <circle cx="8" cy="8" r="7" fill="var(--ink)"/>
      <rect x="4" y="5.5" width="8" height="5.5" fill="none" stroke="#fff" stroke-width="1.2"/>
      <path d="M4 5.5 L8 8.5 L12 5.5" fill="none" stroke="#fff" stroke-width="1.2"/>
    </svg>
    <span>quillmarshimages@postnook.net</span>
  </div>
</section>

</body>
</html>
```